Nutrition product information web site

Nutrition Website (see upload) without Shop function but link to Brivel ASIN number that customer could order from Brivel direct. Content must be easily editable without coding. Web environment must be responsive to support mobile devices as well. design should be modern and clear. loading of web elements must be fast. not too much time consuming features.

Industry/Entity Type

Nutrition

Number of Pages Required

5+ page

Font styles to use
Sans Serif

Colors
33b8a4
9bcb3c
0255a3
0a90cc
a54499

Requirements
Must have
• read attached document
Nice to have
• read attached document
Should not have
• read attached document

```html
<!DOCTYPE html>
<html lang="en">
<head>
<meta charset="utf-8">
<title>Verdalo – Health &amp; Fitness</title>
<link href="https://fonts.googleapis.com/css2?family=Open+Sans:wght@400;600;700&family=Libre+Baskerville:wght@400;700&family=Marcellus&display=swap" rel="stylesheet">
<style>
:root{
  --ink:#231f20;
  --text:#333;
  --muted:#777;
  --line:#dcdcdc;
  --white:#fff;
  --teal:#33b8a4;
  --green:#9bcb3c;
  --blue:#0255a3;
  --sky:#0a90cc;
  --plum:#a54499;
  --alert:#a54499;
}
*{box-sizing:border-box;margin:0;padding:0}
html,body{width:1200px;height:2805px;overflow:hidden}
body{position:relative;background:var(--white);font-family:"Open Sans",Arial,sans-serif;color:var(--text)}
a{color:inherit;text-decoration:none}

/* header */
.util-links{position:absolute;top:12px;left:860px;display:flex;gap:30px;font-size:12px;color:#555}
.util-links span{display:flex;align-items:center;gap:8px}
.util-links i{display:inline-block;width:12px;height:12px;border-radius:50%;background:var(--teal)}
.logo{position:absolute;top:22px;left:120px;width:150px;text-align:center}
.logo .mark{display:block;width:60px;height:60px;margin:0 auto 6px;border:4px solid var(--ink);border-radius:50%}
.logo b{font-weight:700;font-size:24px;letter-spacing:5px;color:var(--ink)}
.search{position:absolute;top:64px;left:514px;width:348px;height:30px;border:1px solid #ccc;border-radius:16px;display:flex;align-items:center;font-size:12px}
.search .cat{width:56px;padding-left:14px;color:#555;border-right:1px solid #ccc}
.search .field{flex:1;padding-left:10px;color:#aaa;font-size:11px}
.search .go{width:62px;height:30px;margin-right:-1px;background:var(--teal);color:#fff;border-radius:16px;display:flex;align-items:center;justify-content:center;font-size:13px}

.main-nav{position:absolute;top:132px;left:0;width:1200px;height:36px;background:var(--ink)}
.main-nav ul{list-style:none;display:flex;position:absolute;left:150px;top:0;height:36px;align-items:center;color:#fff;font-size:13px}
.main-nav li{margin-right:62px;height:36px;line-height:36px}
.main-nav li.active{font-weight:700;box-shadow:inset 0 -3px 0 var(--teal)}
.main-nav .social{position:absolute;left:966px;top:10px;display:flex;gap:24px}
.social i{display:block;width:15px;height:15px;border-radius:50%;background:#fff}

/* hero */
.hero{position:absolute;top:168px;left:0;width:1200px;height:494px;background:linear-gradient(90deg,#f6f6f6 0%,#eeeceb 50%,#e6e1dd 100%)}
.hero .photo{position:absolute;right:0;top:0;width:520px;height:494px;background:linear-gradient(180deg,#e9e2dd 0%,#d9b8a2 40%,#c99c82 62%,#4aa8d6 78%,#3897c9 100%)}
.hero h1{position:absolute;left:122px;top:80px;font-family:"Libre Baskerville",serif;font-weight:400;font-size:36px;color:#1b1b1b}
.hero p{position:absolute;left:122px;top:136px;font-size:26px;color:#222}
.hero .bottles{position:absolute;left:120px;top:200px;width:272px;height:272px;border-radius:10px;background:linear-gradient(180deg,#e4e4e4 0%,#fafafa 30%,#fff 62%,#33b8a4 63%,#33b8a4 66%,#dfe6ea 67%,#dfe6ea 100%)}
.dots{position:absolute;display:flex;gap:6px;align-items:center}
.dots i{width:10px;height:10px;border-radius:50%;border:1px solid #bbb;background:#fff}
.dots i.on{width:14px;height:14px;background:var(--sky);border-color:var(--sky)}

/* sidebar */
.box{position:absolute;left:120px;width:240px;border:1px solid var(--line);background:#fff}
.box h3{font-family:"Libre Baskerville",serif;font-weight:400;font-size:14px;color:#222;padding:10px 12px;border-bottom:1px solid var(--line)}
.ship{position:absolute;left:120px;top:724px;width:240px;height:128px;background:var(--ink);color:#fff;border:3px solid #fff;outline:1px dashed #666;outline-offset:-10px}
.ship svg{position:absolute;left:18px;top:44px;width:46px;height:40px}
.ship b{position:absolute;left:84px;top:42px;font-family:"Libre Baskerville",serif;font-weight:400;font-size:16px}
.ship span{position:absolute;left:84px;top:70px;font-size:12px;color:var(--green)}
.mini{display:flex;gap:14px;padding:14px 12px 0}
.mini .thumb{width:40px;height:60px;border-radius:4px;background:linear-gradient(180deg,#ddd,#fff 40%,#cfe7e2)}
.mini p{font-size:11px;color:#444;margin-top:8px}
.mini strong{display:block;font-size:12px;font-weight:600;margin-top:14px;color:var(--blue)}
.all-link{position:absolute;right:12px;bottom:10px;font-size:9px;text-decoration:underline;font-style:italic;color:#444}
.extra-list{list-style:none;padding:12px 18px;font-size:10px;color:#666;line-height:21px}
.extra-list li::before{content:"›";margin-right:8px;color:var(--teal)}
.testi{text-align:center}
.testi .avatar{width:78px;height:78px;border-radius:50%;margin:18px auto 10px;border:2px solid #333;background:linear-gradient(180deg,#d9d4ce,#c9c2bb)}
.testi b{display:block;font-size:12px}
.testi small{display:block;font-size:10px;color:#777;margin-top:4px}
.testi p{font-size:10px;line-height:16px;color:#555;padding:12px 18px 0}
.ad{position:absolute;left:120px;top:1946px;width:240px;height:310px;background:linear-gradient(160deg,#ccdfe9 0%,#eef3f6 50%,#9dbbd0 100%)}
.ad b{position:absolute;right:28px;top:46px;font-size:19px;color:var(--plum);font-weight:600}
.ad span{position:absolute;right:28px;top:78px;font-size:11px;color:#333}

/* categories */
.cat-card{position:absolute;top:724px;width:222px;text-align:center}
.cat-card .pic{height:172px;border:1px solid var(--line);border-bottom-width:4px}
.cat-card h4{font-family:"Marcellus",serif;font-weight:400;font-size:19px;color:#1b1b1b;margin-top:14px}
.cat-card p{font-size:12px;color:#444;margin-top:2px}

.section-title{position:absolute;left:390px;top:1004px;width:688px;height:46px;border-bottom:1px solid var(--line)}
.section-title h2{font-family:"Libre Baskerville",serif;font-weight:400;font-size:23px;color:#1b1b1b}
.arrows{position:absolute;right:0;top:18px;display:flex;gap:4px}
.arrows span{width:18px;height:16px;border:1px solid #aaa;font-size:10px;line-height:14px;text-align:center}

.product{position:absolute;width:198px;height:278px;border:1px solid var(--line);background:#fff;text-align:center}
.product .pic{position:relative;height:200px;border-bottom:1px solid var(--line);background:linear-gradient(180deg,#f4f4f4,#fff 45%,#e6eeee)}
.product .pic.btn::after{content:"View on Brivel";position:absolute;left:34px;top:88px;width:130px;height:34px;line-height:34px;border-radius:18px;background:var(--teal);color:#fff;font-size:12px;font-weight:600}
.product p{font-size:11px;color:#444;margin-top:22px}
.product strong{display:block;font-weight:600;font-size:12px;margin-top:16px;color:var(--blue)}

.banner{position:absolute;left:390px;top:1734px;width:688px;height:298px;background:linear-gradient(180deg,#9cc4dd 0%,#c7dde3 35%,#7fa85a 65%,#5a8a3c 100%)}
.banner h3{position:absolute;left:16px;top:22px;width:290px;font-family:"Libre Baskerville",serif;font-weight:400;font-size:17px;line-height:24px;color:#1b1b1b;text-align:center}
.banner .cta{position:absolute;left:84px;top:104px;width:122px;height:26px;line-height:26px;border-radius:14px;background:var(--teal);color:#fff;font-size:11px;font-weight:600;text-align:center}
.banner .bottles{position:absolute;left:70px;top:142px;width:150px;height:136px;border-radius:6px;background:linear-gradient(180deg,#e4e4e4,#fff 40%,#cfe2ea)}

.feature{position:absolute;top:2084px;width:140px;text-align:center}
.feature .ic{width:76px;height:76px;margin:0 auto;border:2px solid var(--c);border-radius:50%;display:flex;align-items:center;justify-content:center}
.feature .ic svg{width:36px;height:36px;stroke:var(--c)}
.feature p{font-size:11px;color:#333;margin-top:24px;line-height:19px}

/* footer */
.footer-bg{position:absolute;left:0;top:2284px;width:1200px;height:386px;background:#f7f7f7}
.newsletter{position:absolute;left:120px;top:2296px;width:958px;height:90px;background:var(--ink);color:#fff}
.newsletter svg{position:absolute;left:20px;top:24px;width:50px;height:42px}
.newsletter h2{position:absolute;left:88px;top:30px;font-family:"Marcellus",serif;font-weight:400;font-size:26px;letter-spacing:.5px}
.newsletter .email{position:absolute;left:430px;top:26px;width:348px;height:38px;border-radius:20px;background:#fff;color:#aaa;font-size:10px;padding:13px 20px}
.newsletter .sub{position:absolute;left:690px;top:26px;width:88px;height:38px;border-radius:0 20px 20px 0;background:var(--teal);color:#fff;font-size:13px;line-height:38px;text-align:center}
.newsletter .social{position:absolute;left:854px;top:37px;display:flex;gap:16px}
.newsletter .social i{width:14px;height:14px}

.f-logo{position:absolute;left:122px;top:2432px;display:flex;align-items:center;gap:10px}
.f-logo .mark{width:48px;height:48px;border:3px solid var(--ink);border-radius:50%}
.f-logo b{font-weight:700;font-size:26px;letter-spacing:5px;color:var(--ink)}
.f-about{position:absolute;left:120px;top:2502px;width:350px;font-size:10px;line-height:20px;color:#666}
.f-col{position:absolute;top:2456px}
.f-col h4{font-family:"Marcellus",serif;font-weight:400;font-size:14px;color:#222;margin-bottom:16px;letter-spacing:.5px}
.f-col ul{list-style:none;font-size:10px;line-height:19.5px;color:#666}
.f-col li::before{content:"›";margin-right:8px;color:var(--teal)}
.store li{display:flex;gap:16px;margin-bottom:10px;line-height:14px}
.store li::before{content:none}
.store svg{width:12px;height:14px;flex:none}

.bottom{position:absolute;left:0;top:2670px;width:1200px;height:135px;background:var(--ink);color:#fff;text-align:center}
.bottom nav{margin-top:22px;font-size:11px}
.bottom nav b{font-weight:700}
.bottom nav span{margin:0 14px}
.bottom small{display:block;font-size:10px;margin-top:14px}
</style>
</head>
<body>

<header>
  <div class="util-links">
    <span><i></i>Where to Buy</span><span>USD ⌄</span><span>EN ⌄</span>
  </div>
  <a class="logo" href="#"><span class="mark"></span><b>VERDALO</b></a>
  <div class="search"><span class="cat">All ⌄</span><span class="field">Enter your keyword</span><span class="go">Search</span></div>
</header>

<nav class="main-nav">
  <ul><li class="active">HOME</li><li>ABOUT US</li><li>BLOG</li><li>SITE MAP</li><li>CONTACT</li></ul>
  <div class="social"><i></i><i></i><i></i></div>
</nav>

<section class="hero">
  <div class="photo" role="img" aria-label="Photo of a woman in sportswear measuring her waist with a tape measure"></div>
  <h1>Health &amp; Fitness</h1>
  <p>Your Health Is Our Primary Concern!</p>
  <div class="bottles" role="img" aria-label="Product photo of two supplement bottles"></div>
  <div class="dots" style="left:576px;top:470px"><i></i><i class="on"></i><i></i></div>
</section>

<aside>
  <div class="ship">
    <svg viewBox="0 0 46 40" fill="none" stroke="#fff" stroke-width="2"><rect x="2" y="8" width="26" height="20"/><path d="M28 14h9l7 8v6H28z"/><circle cx="10" cy="31" r="4" fill="#231f20"/><circle cx="36" cy="31" r="4" fill="#231f20"/></svg>
    <b>Order on Brivel</b><span>Delivered direct to you</span>
  </div>

  <div class="box" style="top:880px;height:390px">
    <h3>New Products</h3>
    <div class="mini"><div class="thumb" role="img" aria-label="Supplement bottle"></div><div><p>Quisque malesuada tortor</p><strong>$ 137.00</strong></div></div>
    <div class="mini" style="padding-top:48px"><div class="thumb" role="img" aria-label="Supplement bottle"></div><div><p>Quisque malesuada tortor</p><strong>$ 137.00</strong></div></div>
    <div class="mini" style="padding-top:48px"><div class="thumb" role="img" aria-label="Supplement bottle"></div><div><p>Quisque malesuada tortor</p><strong>$ 137.00</strong></div></div>
    <a class="all-link" href="#">All New Products</a>
  </div>

  <div class="box" style="top:1300px;height:196px">
    <h3>Extra</h3>
    <ul class="extra-list"><li>About Us</li><li>Where to Buy</li><li>Privacy Policy</li><li>Nutrition Facts</li><li>Contact Us</li><li>Site Map</li></ul>
  </div>

  <div class="box testi" style="top:1536px;height:384px">
    <h3 style="text-align:left">Testimonials</h3>
    <div class="avatar" role="img" aria-label="Customer portrait photo"></div>
    <b>Quisque Malesuada</b><small>Producer</small>
    <p>Lorem ipsum dolor sit amet, consectetur adipiscing elit. Suspendisse sit amet leo a augue feugiat placerat quis at massa. Donec at sapien ante. Morbi pretium ex non sapien posuere consequat. Sed semper, orci a tempor congue, nunc quam interdum diam, a interdum ligula.</p>
    <div class="dots" style="left:100px;top:344px"><i></i><i style="background:var(--sky);border-color:var(--sky)"></i><i></i></div>
  </div>

  <div class="ad" role="img" aria-label="Photo of a scientist using a laboratory microscope"><b>EQUIPMENTS</b><span>GET 20% OFF</span></div>
</aside>

<main>
  <div class="cat-card" style="left:390px"><div class="pic" role="img" aria-label="Photo of a smiling couple on a beach" style="background:linear-gradient(180deg,#cfe0ea,#e7dccd 60%,#d8c4a8);border-bottom-color:var(--teal)"></div><h4>SMART LIVING</h4><p>Nutrition Supplements</p></div>
  <div class="cat-card" style="left:623px"><div class="pic" role="img" aria-label="Photo of a woman exercising on a white floor" style="background:linear-gradient(180deg,#f2f2f2,#e4e4e6 60%,#b9c3cf);border-bottom-color:var(--green)"></div><h4>SMART DIETING</h4><p>Dieting Supplements</p></div>
  <div class="cat-card" style="left:856px"><div class="pic" role="img" aria-label="Photo of a group fitness class" style="background:linear-gradient(180deg,#c69a78,#d86c8c 55%,#6b4c3e);border-bottom-color:var(--plum)"></div><h4>SMART BODY</h4><p>Sport Supplements</p></div>

  <div class="section-title"><h2>Featured Products</h2><div class="arrows"><span>‹</span><span>›</span></div></div>

  <div class="product" style="left:390px;top:1088px"><div class="pic btn" role="img" aria-label="Supplement bottle photo"></div><p>Quisque malesuada tortor ut</p><strong>$ 137.00</strong></div>
  <div class="product" style="left:634px;top:1088px"><div class="pic" role="img" aria-label="Supplement bottle photo"></div><p>Quisque malesuada tortor ut</p><strong>$ 309.00</strong></div>
  <div class="product" style="left:880px;top:1088px"><div class="pic" role="img" aria-label="Supplement bottle photo"></div><p>Quisque malesuada tortor ut</p><strong>$ 309.00</strong></div>
  <div class="product" style="left:390px;top:1396px"><div class="pic" role="img" aria-label="Supplement bottle photo"></div><p>Quisque malesuada tortor ut</p><strong>$ 137.00</strong></div>
  <div class="product" style="left:634px;top:1396px"><div class="pic" role="img" aria-label="Supplement bottle photo"></div><p>Quisque malesuada tortor ut</p><strong>$ 309.00</strong></div>
  <div class="product" style="left:880px;top:1396px"><div class="pic" role="img" aria-label="Supplement bottle photo"></div><p>Quisque malesuada tortor ut</p><strong>$ 309.00</strong></div>

  <div class="banner" role="img" aria-label="Photo of a family jogging together across a green meadow">
    <h3>Morbi pretium ex non sapien posuere consequat sed semper orcia tempor.</h3>
    <span class="cta">View on Brivel</span>
    <div class="bottles"></div>
  </div>

  <div class="feature" style="left:386px;--c:var(--green)"><div class="ic"><svg viewBox="0 0 36 36" fill="none" stroke-width="2.4"><path d="M8 30C8 14 18 6 30 6c0 14-8 22-22 24z"/><path d="M8 30L22 16"/></svg></div><p>CERTIFIED ORGANIC<br>CULTIVATION</p></div>
  <div class="feature" style="left:522px;--c:var(--teal)"><div class="ic"><svg viewBox="0 0 36 36" fill="none" stroke-width="2.4"><path d="M24 12L6 30l6-20z"/><path d="M24 12l6-6M24 12l7 1M24 12l-1-7"/></svg></div><p>100% RAW FOOD<br>QUALITY</p></div>
  <div class="feature" style="left:662px;--c:var(--sky)"><div class="ic"><svg viewBox="0 0 36 36" fill="none" stroke-width="2.4"><path d="M9 4h13l6 6v22H9z"/><path d="M13 14h10M13 19h10M13 24h7"/></svg></div><p>HIGH NUTRIENT<br>CONTENT</p></div>
  <div class="feature" style="left:802px;--c:var(--blue)"><div class="ic"><svg viewBox="0 0 36 36" fill="none" stroke-width="2.4"><rect x="6" y="12" width="12" height="18" rx="2"/><rect x="8" y="7" width="8" height="5"/><rect x="20" y="16" width="10" height="14" rx="2"/><path d="M10 21h4M12 19v4"/></svg></div><p>EASY AND VERSATILE<br>USE</p></div>
  <div class="feature" style="left:942px;--c:var(--plum)"><div class="ic"><svg viewBox="0 0 36 36" fill="none" stroke-width="2.4"><circle cx="22" cy="7" r="3"/><path d="M20 12l-5 9 6 4-3 8M15 21l-6 5M20 12l7 6"/></svg></div><p>RICH IN<br>VITAMINS</p></div>
</main>

<footer>
  <div class="footer-bg"></div>
  <div class="newsletter">
    <svg viewBox="0 0 50 42" fill="none" stroke="#fff" stroke-width="2"><path d="M4 16l21-13 21 13v24H4z"/><path d="M4 16l21 14 21-14"/><rect x="12" y="8" width="26" height="16"/></svg>
    <h2>SIGN UP TO NEWSLETTER</h2>
    <div class="email">Enter your email</div><div class="sub">Subscribe</div>
    <div class="social"><i></i><i></i><i></i></div>
  </div>

  <div class="f-logo"><span class="mark"></span><b>VERDALO</b></div>
  <p class="f-about">Lorem ipsum dolor sit amet, consectetur adipiscing elit. Suspendisse sit amet leo a augue feugiat placerat quis at massa. Donec at sapien ante. Morbi pretium ex non sapien posuere consequat. Sed semper, orci a tempor congue, nunc quam interdum diam, a interdum ligula nunc at massa. Mauris quis nisl lobortis, dapibus dolor finibus, mollis eget metus tincidunt, sagittis quam lacus.</p>

  <div class="f-col" style="left:524px"><h4>EXTRA</h4><ul><li>About Us</li><li>Where to Buy</li><li>Privacy Policy</li><li>Nutrition Facts</li><li>Contact Us</li><li>Site Map</li></ul></div>
  <div class="f-col" style="left:710px"><h4>PRODUCTS</h4><ul><li>Nutrition</li><li>Dieting</li><li>Sport</li><li>New Products</li></ul></div>
  <div class="f-col store" style="left:880px"><h4>STORE INFORMATION</h4>
    <ul>
      <li><svg viewBox="0 0 12 14"><path d="M6 0a5 5 0 015 5c0 4-5 9-5 9S1 9 1 5a5 5 0 015-5z" fill="#33b8a4"/><circle cx="6" cy="5" r="2" fill="#fff"/></svg><span>Verdalo Nutrition Research Ltd<br>Lindenweg 14/B/2<br>4020 Talheim<br>Austria</span></li>
      <li><svg viewBox="0 0 12 14"><path d="M2 1l3 0 1 3-2 1c1 2 2 3 4 4l1-2 3 1v3c-6 0-10-4-10-10z" fill="#33b8a4"/></svg><span>+00 555 014 2290</span></li>
      <li><svg viewBox="0 0 12 14"><rect x="0" y="3" width="12" height="8" fill="#33b8a4"/><path d="M0 3l6 5 6-5" stroke="#fff" fill="none"/></svg><span>info@verdalo-research.example</span></li>
    </ul>
  </div>

  <div class="bottom">
    <nav><b>HOME</b><span>|</span>ABOUT US<span>|</span>BLOG<span>|</span>SITE MAP<span>|</span>CONTACT</nav>
    <small>Copyright © 2017 VERDALO.EXAMPLE. All Rights Reserved.</small>
  </div>
</footer>

</body>
</html>
```